Website To Serve As A Resource For Medical Conditions

I need a website that is attractive that will be utilized to educate patients on either hepatitis c or HIV so it should be easily readable attractive but also professional. This website is going to be furnished with various topics for example, HIV treatment, HIV and Nutrition, HIV and Exercise, HIV and....

This website will also be cloned and utilized similarly for Hepatitis.

Coded - Design and coding required

1 page

0094D4
00A9DD
6FCCEA
C7EBF8
E9F6FB
A7469A
B969AE
D3A5CF
EDDBEB
F8F0F9
6B429C
8869AF
B7A5CE
E3DAEB
F3F0F8

```html
<!DOCTYPE html>
<html lang="en">
<head>
<meta charset="UTF-8">
<title>Lorem Ipsum – HIV Patient Resource</title>
<link href="https://fonts.googleapis.com/css2?family=Montserrat:wght@400;500;600;700;800&family=Open+Sans:wght@400;600&display=swap" rel="stylesheet">
<style>
:root{
  --blue-700:#0094D4;--blue-500:#00A9DD;--blue-300:#6FCCEA;--blue-100:#C7EBF8;--blue-50:#E9F6FB;
  --pink-700:#A7469A;--pink-500:#B969AE;--pink-300:#D3A5CF;--pink-100:#EDDBEB;--pink-50:#F8F0F9;
  --violet-700:#6B429C;--violet-500:#8869AF;--violet-300:#B7A5CE;--violet-100:#E3DAEB;--violet-50:#F3F0F8;
  --ink:#1d1d1f;--text:#555;--footer:#111;
}
*{margin:0;padding:0;box-sizing:border-box}
html,body{width:1200px;height:5272px;overflow:hidden}
body{position:relative;font-family:"Open Sans",sans-serif;color:var(--text);background:#fff}
h1,h2,h3,h4,.btn,.nav,.brand{font-family:"Montserrat",sans-serif}
.abs{position:absolute}
p{font-size:14px;line-height:1.65}

/* top bar */
.topbar{position:absolute;top:0;left:0;width:1200px;height:32px;background:var(--blue-700);color:#fff;font-size:11px;display:flex;align-items:center;justify-content:space-between;padding:0 40px 0 160px}
.topbar .social{display:flex;align-items:center;gap:8px}
.topbar .social i{display:block;width:18px;height:18px;border-radius:50%;background:#fff}
/* nav */
.header{position:absolute;top:32px;left:0;width:1200px;height:80px;background:#fff;display:flex;align-items:center;justify-content:space-between;padding:0 40px 0 120px}
.brand{display:flex;align-items:center;gap:10px;font-weight:800;font-size:20px;color:var(--ink)}
.brand i{width:26px;height:26px;background:var(--blue-700);display:block}
.nav{display:flex;gap:48px;font-size:14px;font-weight:500;color:var(--ink)}
.nav .active{border-bottom:2px solid var(--blue-700);padding-bottom:6px;font-weight:700}
/* hero */
.hero{position:absolute;top:112px;left:0;width:1200px;height:748px;background:linear-gradient(120deg,#7fc4e6 0%,#cfe9f5 40%,#9ccbe4 70%,#4aa6d6 100%)}
.hero-shade{position:absolute;inset:0;background:linear-gradient(180deg,rgba(0,148,212,.15),rgba(0,148,212,.55))}
.hero h1{position:absolute;top:215px;width:100%;text-align:center;color:#fff;font-size:50px;font-weight:800;line-height:1.1}
.hero p{position:absolute;top:345px;width:100%;text-align:center;color:#fff;font-size:15px}
.btn{display:inline-block;font-size:12px;font-weight:700;letter-spacing:.5px;padding:12px 30px}
.btn-white{background:#fff;color:var(--ink)}
.btn-blue{background:var(--blue-700);color:#fff}
.hero .btn{position:absolute;top:408px;left:518px}
.hero .arrow{position:absolute;top:335px}
.wave{position:absolute;left:0;top:720px}
.dot{position:absolute;top:832px;left:590px;width:20px;height:32px;border-radius:10px;background:var(--blue-700)}
/* about */
.about h2{position:absolute;left:120px;top:960px;font-size:46px;font-weight:800;color:var(--ink)}
.about .copy{position:absolute;left:120px;top:1030px;width:440px}
.about .copy p+p{margin-top:18px}
.about .btn{position:absolute;left:120px;top:1330px}
.about .frame{position:absolute;left:620px;top:960px;width:480px;height:520px;border:2px solid var(--blue-700)}
.about .photo{position:absolute;left:600px;top:940px;width:480px;height:500px;background:linear-gradient(135deg,#c9dbe6,#f1eee9 50%,#8fb4cc)}
/* services */
.services{position:absolute;top:1580px;left:0;width:1200px;height:720px;background:linear-gradient(120deg,var(--pink-500),var(--pink-700) 60%,#9c3c90)}
.services .ribbon{position:absolute;left:560px;top:40px;width:380px;height:640px;background:linear-gradient(160deg,rgba(216,60,120,.5),rgba(160,30,80,.35));border-radius:190px 190px 40px 40px}
.services h2{position:absolute;top:108px;width:100%;text-align:center;color:#fff;font-size:46px;font-weight:800}
.services .lead{position:absolute;top:170px;left:320px;width:560px;text-align:center;color:#fff;font-size:13px}
.svc{position:absolute;top:270px;width:250px;color:#fff}
.svc .ico{width:56px;height:56px;border-radius:50%;background:#fff;display:flex;align-items:center;justify-content:center}
.svc h3{margin-top:24px;font-size:16px;font-weight:800}
.svc p{margin-top:10px;font-size:12px;color:rgba(255,255,255,.85)}
.services .btn{position:absolute;top:575px;left:518px}
/* why */
.why .photo{position:absolute;left:80px;top:2400px;width:480px;height:680px;background:linear-gradient(180deg,#f6f7f8,#dfe8ee 60%,#c0d2de)}
.why h2{position:absolute;left:628px;top:2480px;font-size:46px;font-weight:800;color:var(--ink)}
.why .lead{position:absolute;left:628px;top:2545px;width:460px}
.reason{position:absolute;left:608px;width:480px;display:flex;gap:22px}
.reason .num{font-family:"Montserrat",sans-serif;font-size:58px;font-weight:500;color:var(--blue-700);line-height:1;width:60px}
.reason h4{font-size:15px;font-weight:700;color:var(--ink);margin-bottom:6px}
/* testimonials */
.testi{position:absolute;top:3200px;left:0;width:1200px;height:680px;background:linear-gradient(120deg,var(--violet-300),var(--pink-300) 50%,var(--violet-300))}
.testi .ribbon{position:absolute;left:640px;top:40px;width:360px;height:600px;background:linear-gradient(160deg,rgba(200,40,110,.45),rgba(150,30,80,.3));border-radius:180px 180px 40px 40px}
.testi h2{position:absolute;top:100px;width:100%;text-align:center;color:#fff;font-size:46px;font-weight:800}
.card{position:absolute;background:#fff;padding:50px 30px 30px;text-align:center}
.card p{font-size:12px}
.card .q{position:absolute;top:-40px;left:50%;transform:translateX(-50%)}
.card.main p{font-size:14px}
.testi .avatar{position:absolute;left:574px;top:520px;width:52px;height:52px;border-radius:50%;background:linear-gradient(135deg,#e6c6a8,#8a5a4a);border:3px solid #fff}
.testi .name{position:absolute;top:582px;width:100%;text-align:center;font-size:12px;color:#fff;font-weight:600}
.circle-arrow{position:absolute;width:36px;height:36px;border-radius:50%;display:flex;align-items:center;justify-content:center}
/* blogs */
.blogs h2{position:absolute;left:140px;top:3990px;font-size:46px;font-weight:800;color:var(--ink)}
.post{position:absolute;top:4110px;width:280px;height:390px;background:#fff;box-shadow:0 6px 24px rgba(0,0,0,.1)}
.post .thumb{height:180px}
.post h4{margin:22px 20px 6px;text-align:center;font-size:14px;font-weight:700;color:var(--ink)}
.post .date{text-align:center;font-size:11px;color:var(--blue-700);font-weight:600;font-family:"Montserrat",sans-serif}
.post p{margin:16px 24px 0;text-align:center;font-size:12px}
.post .more{position:absolute;left:80px;bottom:24px;font-family:"Montserrat",sans-serif;font-size:12px;font-weight:700;color:var(--blue-700)}
/* partners */
.partner{position:absolute;top:4575px;height:110px;background:#f2f2f2;display:flex;align-items:center;justify-content:center}
.partner i{display:block;width:90px;height:40px;border-radius:6px;background:#c8c8c8}
/* footer */
.footer{position:absolute;top:4740px;left:0;width:1200px;height:532px;background:var(--footer);color:#ddd}
.footer .brand{position:absolute;left:140px;top:140px;color:#fff}
.footer .brand i{background:var(--blue-700)}
.footer .about-text{position:absolute;left:140px;top:200px;width:300px;font-size:12px;color:#ccc}
.footer ul{position:absolute;top:148px;list-style:none;font-size:12px;line-height:2;color:#ddd}
.footer .rule{position:absolute;left:140px;right:140px;top:470px;height:1px;background:#444}
.footer .copy{position:absolute;top:490px;width:100%;text-align:center;font-size:11px;color:#aaa}
</style>
</head>
<body>

<div class="topbar">
  <span>Helpline Number: +1 555 0100 &nbsp;|&nbsp; Mon–Sat 9:00 – 18:00</span>
  <span class="social">Follow Us On: <i></i><i></i><i></i><i></i></span>
</div>

<header class="header">
  <div class="brand"><i></i>LOREM IPSUM</div>
  <nav class="nav"><span class="active">Home</span><span>About Us</span><span>Services</span><span>Testimonials</span><span>Blogs</span><span>Contact Us</span></nav>
</header>

<section class="hero">
  <div class="hero-shade" role="img" aria-label="Doctor attending a patient in a bright clinic room"></div>
  <h1>YOUR PARTNER IN HEALTH<br>AND HOPE</h1>
  <p>Lorem Ipsum is simply dummy text of the printing and typesetting industry.<br>Lorem Ipsum has been the industry's standard.</p>
  <span class="btn btn-white">LEARN MORE</span>
  <svg class="arrow" style="left:70px" width="80" height="14"><path d="M2 7H78M2 7l8-6M2 7l8 6" stroke="#fff" stroke-width="2" fill="none"/></svg>
  <svg class="arrow" style="right:70px" width="80" height="14"><path d="M2 7H78M78 7l-8-6M78 7l-8 6" stroke="#fff" stroke-width="2" fill="none"/></svg>
  <svg class="wave" width="1200" height="30" viewBox="0 0 1200 30" preserveAspectRatio="none"><path d="M0 10Q300 40 600 20T1200 10V30H0Z" fill="#fff"/></svg>
</section>
<div class="dot"></div>

<section class="about">
  <h2>ABOUT US</h2>
  <div class="copy">
    <p>Lorem Ipsum is simply dummy text of the printing and typesetting industry. Lorem Ipsum has been the industry's standard dummy text ever since the 1500s.Lorem Ipsum is simply dummy text of the printing and typesetting industry. Lorem Ipsum has been the industry's standard dummy text ever since the 1500s.</p>
    <p>Lorem Ipsum is simply dummy text of the printing and typesetting industry. Lorem Ipsum has been the industry's standard dummy text ever since the 1500s.</p>
  </div>
  <span class="btn btn-blue">READ MORE</span>
  <div class="frame"></div>
  <div class="photo" role="img" aria-label="Doctor discussing a chart with a patient in a hospital corridor"></div>
</section>

<section class="services">
  <div class="ribbon" role="img" aria-label="Awareness ribbon on a textured background"></div>
  <h2>SERVICES WE OFFER</h2>
  <p class="lead">Lorem Ipsum is simply dummy text of the printing and typesetting industry. Lorem Ipsum has been the industry's standard dummy text ever since the 1500s.</p>
  <div class="svc" style="left:120px"><div class="ico"><svg width="26" height="26" viewBox="0 0 26 26"><path d="M13 2v22M2 13h22" stroke="#A7469A" stroke-width="6"/></svg></div><h3>HIV TREATMENT</h3><p>Lorem Ipsum is simply dummy text of the printing and typesetting industry. Lorem Ipsum has been the industry's standard dummy text ever since the 1500s.</p></div>
  <div class="svc" style="left:375px"><div class="ico"><svg width="26" height="26" viewBox="0 0 26 26"><circle cx="13" cy="15" r="9" fill="#A7469A"/><path d="M13 6c0-3 3-4 5-4" stroke="#A7469A" stroke-width="2" fill="none"/></svg></div><h3>HIV AND NUTRITION</h3><p>Lorem Ipsum is simply dummy text of the printing and typesetting industry. Lorem Ipsum has been the industry's standard dummy text ever since the 1500s.</p></div>
  <div class="svc" style="left:630px"><div class="ico"><svg width="26" height="26" viewBox="0 0 26 26"><rect x="5" y="3" width="16" height="20" rx="2" fill="#A7469A"/><path d="M9 9h8M9 13h8M9 17h8" stroke="#fff" stroke-width="2"/></svg></div><h3>HIV AND EXERCISE</h3><p>Lorem Ipsum is simply dummy text of the printing and typesetting industry. Lorem Ipsum has been the industry's standard dummy text ever since the 1500s.</p></div>
  <div class="svc" style="left:885px"><div class="ico"><svg width="26" height="26" viewBox="0 0 26 26"><circle cx="13" cy="13" r="7" fill="#A7469A"/><path d="M13 1v5M13 20v5M1 13h5M20 13h5M4.5 4.5l3.5 3.5M18 18l3.5 3.5M4.5 21.5l3.5-3.5M18 8l3.5-3.5" stroke="#A7469A" stroke-width="2.5"/></svg></div><h3>HIV AND PRODUCT</h3><p>Lorem Ipsum is simply dummy text of the printing and typesetting industry. Lorem Ipsum has been the industry's standard dummy text ever since the 1500s.</p></div>
  <span class="btn btn-white">LEARN MORE</span>
</section>

<section class="why">
  <div class="photo" role="img" aria-label="Smiling doctor in a white coat with a stethoscope giving a thumbs up"></div>
  <h2>WHY CHOOSE US?</h2>
  <p class="lead">Lorem Ipsum is simply dummy text of the printing and typesetting industry. Lorem Ipsum has been the industry's standard dummy text ever since.</p>
  <div class="reason" style="top:2665px"><span class="num">01</span><div><h4>Over 20 years of experience.</h4><p>Lorem Ipsum is simply dummy text of the printing and typesetting industry. Lorem Ipsum has been the industry.</p></div></div>
  <div class="reason" style="top:2785px"><span class="num">02</span><div><h4>We have experienced Doctor's.</h4><p>Lorem Ipsum is simply dummy text of the printing and typesetting industry. Lorem Ipsum has been the industry.</p></div></div>
  <div class="reason" style="top:2905px"><span class="num">03</span><div><h4>We are improving everyday.</h4><p>Nunc fringilla eros vitae nisl posuere, at consectetur nulla feugiat. Nullam at mauris vitae tortor sodales efficitur.</p></div></div>
</section>

<section class="testi">
  <div class="ribbon" role="img" aria-label="Awareness ribbon on a soft violet background"></div>
  <h2>WHAT PATIENT SAYS</h2>
  <div class="circle-arrow" style="left:78px;top:345px;background:rgba(255,255,255,.35)"><svg width="12" height="12"><path d="M8 1L3 6l5 5" stroke="#555" stroke-width="2" fill="none"/></svg></div>
  <div class="circle-arrow" style="left:1086px;top:345px;background:rgba(255,255,255,.35)"><svg width="12" height="12"><path d="M4 1l5 5-5 5" stroke="#555" stroke-width="2" fill="none"/></svg></div>
  <div class="card" style="left:140px;top:275px;width:270px;height:190px">
    <svg class="q" width="70" height="50" viewBox="0 0 70 50"><path d="M4 46V26C4 12 12 4 26 2v10c-8 2-10 8-10 14h10v20ZM40 46V26C40 12 48 4 62 2v10c-8 2-10 8-10 14h10v20Z" fill="#A7469A"/></svg>
    <p>Lorem Ipsum is simply dummy text of the printing and typesetting industry. Lorem Ipsum has been the industry's standard dummy text ever since the 1500s, when an unknown printer took a galley of type.</p>
  </div>
  <div class="card main" style="left:430px;top:225px;width:340px;height:270px">
    <svg class="q" width="90" height="64" viewBox="0 0 70 50"><path d="M4 46V26C4 12 12 4 26 2v10c-8 2-10 8-10 14h10v20ZM40 46V26C40 12 48 4 62 2v10c-8 2-10 8-10 14h10v20Z" fill="#A7469A"/></svg>
    <p>Lorem Ipsum is simply dummy text of the printing and typesetting industry. Lorem Ipsum has been the industry's standard dummy text ever since the 1500s, when an unknown printer took a galley of type.</p>
  </div>
  <div class="card" style="left:790px;top:275px;width:270px;height:190px">
    <svg class="q" width="70" height="50" viewBox="0 0 70 50"><path d="M4 46V26C4 12 12 4 26 2v10c-8 2-10 8-10 14h10v20ZM40 46V26C40 12 48 4 62 2v10c-8 2-10 8-10 14h10v20Z" fill="#A7469A"/></svg>
    <p>Lorem Ipsum is simply dummy text of the printing and typesetting industry. Lorem Ipsum has been the industry's standard dummy text ever since the 1500s, when an unknown printer took a galley of type.</p>
  </div>
  <div class="avatar" role="img" aria-label="Patient portrait"></div>
  <div class="name">Clara Benton</div>
</section>

<section class="blogs">
  <h2>OUR BLOGS</h2>
  <div class="circle-arrow" style="left:960px;top:3998px;border:2px solid #ddd;background:#fff"><svg width="12" height="12"><path d="M8 1L3 6l5 5" stroke="#0094D4" stroke-width="2" fill="none"/></svg></div>
  <div class="circle-arrow" style="left:1010px;top:3998px;background:var(--blue-700)"><svg width="12" height="12"><path d="M4 1l5 5-5 5" stroke="#fff" stroke-width="2" fill="none"/></svg></div>
  <article class="post" style="left:140px"><div class="thumb" role="img" aria-label="Doctor examining a patient" style="background:linear-gradient(135deg,#d9e4ea,#b9cad6)"></div><h4>Lorem Ipsum is simply dummy...</h4><div class="date">APRIL 28, 2022</div><p>Lorem Ipsum is simply dummy text of the printing and typesetting industry.</p><span class="more">READ MORE &nbsp;→</span></article>
  <article class="post" style="left:460px"><div class="thumb" role="img" aria-label="Medical team at work in a clinic" style="background:linear-gradient(135deg,#cfe3f0,#7fb2d3)"></div><h4>Lorem Ipsum is simply dummy...</h4><div class="date">APRIL 28, 2022</div><p>Lorem Ipsum is simply dummy text of the printing and typesetting industry.</p><span class="more">READ MORE &nbsp;→</span></article>
  <article class="post" style="left:780px"><div class="thumb" role="img" aria-label="Nurse caring for a patient in bed" style="background:linear-gradient(135deg,#f3c9a0,#e08c50 60%,#c9dbe6)"></div><h4>Lorem Ipsum is simply dummy...</h4><div class="date">APRIL 28, 2022</div><p>Lorem Ipsum is simply dummy text of the printing and typesetting industry.</p><span class="more">READ MORE &nbsp;→</span></article>
</section>

<section class="partners">
  <div class="partner" style="left:130px;width:200px;background:#fff;box-shadow:0 4px 16px rgba(0,0,0,.08)"><i style="background:var(--blue-100)"></i></div>
  <div class="partner" style="left:380px;width:200px"><i></i></div>
  <div class="partner" style="left:615px;width:205px"><i></i></div>
  <div class="partner" style="left:855px;width:205px"><i></i></div>
</section>

<footer class="footer">
  <div class="brand"><i></i>LOREM IPSUM</div>
  <p class="about-text">Lorem Ipsum is simply dummy text of the printing and typesetting industry. Lorem Ipsum has been the industry's standard dummy text ever since the 1500s.Lorem Ipsum is simply dummy text of the printing and typesetting industry.</p>
  <ul style="left:530px"><li>Investors</li><li>Careers</li><li>Media</li><li>Partners</li></ul>
  <ul style="left:700px"><li>Grant Seekers</li><li>Healthcare Professionals</li><li>Business to Business</li><li>Merchandise</li></ul>
  <ul style="left:950px"><li>Privacy Statement</li><li>Terms of Use</li><li>Site Map</li><li>Contact Us</li></ul>
  <div class="rule"></div>
  <div class="copy">© 2020 Northwind Health Inc. All rights reserved</div>
</footer>

</body>
</html>
```